Business Card Design for Flood Rescue 360 - Property Restoration Professionals

I need a business card designed for Flood Rescue 360. We are a full-service property restoration solution. Providing water, fire, smoke & storm restoration as well as mold remediation and full remodel or reconstruction to homes and businesses across Dallas-Fort Worth, TX.
Target Market(s)
home and business owners with insurance covered property damage from water, fire or storm related damage
Industry/Entity Type
property restoration
Contact Information for Business Card
Martin Kell General Manager Cell: 214-555-0193 Office: 469-555-0148 email: Martin@FloodRescue360.example services: Water, Fire, Mold, Reconstruction Tagline: Urgency for Your Water Emergency!
Look and feel
Each slider illustrates characteristics of the customer's brand and the style your logo design should communicate.

```html
<!DOCTYPE html>
<html lang="en">
<head>
<meta charset="UTF-8">
<title>Flood Rescue 360 – Business Card</title>
<link href="https://fonts.googleapis.com/css2?family=Roboto:wght@400;500;700&display=swap" rel="stylesheet">
<style>
  :root {
    --page-bg: #d3d4d6;
    --brand-blue: #17a9df;
    --brand-blue-light: #3bc3ee;
    --brand-blue-deep: #0aa0d8;
    --ink-grey: #5d5f63;
    --rule-grey: #8a8c90;
    --card-white: #ffffff;
    --drop-tint: #eceff2;
  }
  * { margin: 0; padding: 0; box-sizing: border-box; }
  html, body {
    width: 900px; height: 1200px; overflow: hidden;
    background: var(--page-bg);
    font-family: "Roboto", Arial, sans-serif;
  }
  .card {
    position: absolute; left: 133px; width: 633px; height: 365px; overflow: hidden;
  }
  .card-front { top: 210px; }
  .card-back { top: 624px; background: var(--card-white); }
  .droplet-texture { position: absolute; inset: 0; }
  .card-front .droplet-texture {
    background: radial-gradient(ellipse at 35% 30%, var(--brand-blue-light), var(--brand-blue-deep) 75%);
  }
  .card-back .droplet-texture {
    background: radial-gradient(ellipse at 50% 45%, var(--card-white) 30%, var(--drop-tint) 100%);
  }
  .front-wordmark {
    position: absolute; left: 0; right: 0; top: 110px;
    text-align: center; color: var(--card-white);
    font-weight: 700; font-size: 60px; line-height: 62px; letter-spacing: -1px;
  }
  .front-tagline {
    position: absolute; left: 0; right: 0; top: 312px;
    text-align: center; color: var(--card-white);
    font-weight: 700; font-size: 16px; letter-spacing: 1.2px;
  }
  .back-wordmark {
    position: absolute; left: 52px; top: 142px; width: 255px;
    color: var(--brand-blue); font-weight: 700;
    font-size: 38px; line-height: 40px; letter-spacing: -0.5px;
  }
  .divider {
    position: absolute; left: 317px; top: 105px; width: 2px; height: 152px;
    background: var(--rule-grey);
  }
  .contact-block { position: absolute; left: 336px; top: 103px; }
  .person-name {
    color: var(--brand-blue); font-weight: 500; font-size: 24px; letter-spacing: 0.5px;
  }
  .person-role { color: var(--ink-grey); font-size: 14px; margin-top: 4px; }
  .contact-list { list-style: none; margin-top: 14px; }
  .contact-list li {
    display: flex; align-items: center; gap: 7px;
    color: var(--ink-grey); font-size: 14px; height: 24.5px; letter-spacing: 0.6px;
  }
  .contact-list li.phone { letter-spacing: 2.2px; }
  .contact-list svg { width: 14px; height: 14px; fill: var(--brand-blue); flex: none; }
  .services {
    position: absolute; left: 0; right: 0; top: 306px;
    text-align: center; font-size: 16px; color: var(--ink-grey); font-weight: 500;
  }
  .services .label, .services .sep { color: var(--brand-blue); }
</style>
</head>
<body>
  <section class="card card-front">
    <div class="droplet-texture" role="img" aria-label="Blue surface covered in water droplets"></div>
    <div class="front-wordmark">FLOOD<br>RESCUE 360</div>
    <p class="front-tagline">URGENCY FOR YOUR WATER EMERGENCY!</p>
  </section>

  <section class="card card-back">
    <div class="droplet-texture" role="img" aria-label="White surface covered in faint water droplets"></div>
    <div class="back-wordmark">FLOOD<br>RESCUE 360</div>
    <div class="divider"></div>
    <div class="contact-block">
      <h1 class="person-name">MARTIN KELL</h1>
      <p class="person-role">General Manager</p>
      <ul class="contact-list">
        <li class="phone">
          <svg viewBox="0 0 24 24"><path d="M6.6 10.8a15 15 0 0 0 6.6 6.6l2.2-2.2c.3-.3.7-.4 1-.2 1.1.4 2.3.6 3.6.6.6 0 1 .4 1 1V20c0 .6-.4 1-1 1A17 17 0 0 1 3 4c0-.6.4-1 1-1h3.5c.6 0 1 .4 1 1 0 1.3.2 2.5.6 3.6.1.3 0 .7-.2 1z"/></svg>
          469-555-0148
        </li>
        <li class="phone">
          <svg viewBox="0 0 24 24"><path d="M7 1h10a2 2 0 0 1 2 2v18a2 2 0 0 1-2 2H7a2 2 0 0 1-2-2V3a2 2 0 0 1 2-2zm0 3v14h10V4zm5 15.2a1 1 0 1 0 0 2 1 1 0 0 0 0-2z"/></svg>
          214-555-0193
        </li>
        <li>
          <svg viewBox="0 0 24 24"><path d="M2 5h20v14H2zm2 2v.5l8 5 8-5V7l-8 5z"/></svg>
          Martin@FloodRescue360.example
        </li>
        <li>
          <svg viewBox="0 0 24 24"><path d="M12 2a10 10 0 1 0 0 20 10 10 0 0 0 0-20zm6.9 6h-3a15 15 0 0 0-1.3-3.9A8 8 0 0 1 18.9 8zM12 4c.8 1.2 1.5 2.5 1.9 4h-3.8c.4-1.5 1.1-2.8 1.9-4zM4.3 14a8 8 0 0 1 0-4h3.4a16 16 0 0 0 0 4zm.8 2h3a15 15 0 0 0 1.3 3.9A8 8 0 0 1 5.1 16zm3-8h-3a8 8 0 0 1 4.3-3.9C8.8 5.3 8.4 6.6 8.1 8zM12 20c-.8-1.2-1.5-2.5-1.9-4h3.8c-.4 1.5-1.1 2.8-1.9 4zm2.3-6H9.7a14 14 0 0 1 0-4h4.6a14 14 0 0 1 0 4zm.3 5.9c.6-1.2 1-2.5 1.3-3.9h3a8 8 0 0 1-4.3 3.9zm1.7-5.9a16 16 0 0 0 0-4h3.4a8 8 0 0 1 0 4z"/></svg>
          www.FloodRescue360.example
        </li>
      </ul>
    </div>
    <p class="services"><span class="label">Our Services:</span> Water <span class="sep">|</span> Fire <span class="sep">|</span> Mold <span class="sep">|</span> Reconstruction</p>
  </section>
</body>
</html>
```